Online Banner and skyscrapper ads

Design ads for real estate company in Australia to be used on Plot fnder.com.au details below
sizes
Leaderboard Specifications
• Dimensions: 728×90px
• Format: HTML5 or Animated/Static Gif
• Max file size: 100kb (HTML5), 80kb (GIF, JPG, PNG)
• Back-up image: 40kb (GIF, JPG, PNG). Back-up image only required if you supply an HTML5 banner.
• Looping: Yes
• See Leaderboard for more information.
Email Alert Strip Ad (EASA) Specifications
• Dimensions: 472×114 px
• Format: JPEG, PNG or Static GIF
• File Size: 20kb
• Looping: No
Skyscraper Specifications
• Dimensions: 160x600px
• Looping: Yes
• See Skyscraper for more information.
Mega Skyscraper Specifications
• Dimensions: 300x600px
• Format: HTML5 or Animated/Static GIF
• File size: 100kb (Html5) or 80kb (GIF, JPG, PNG)
• Back-up image: 40kb (JPG or PNG). Back-up image only required if you supply an HTML5 banner.
• Looping: Yes
• See Half Page for more information.

I would like them to be quite simple , WYNDALE Your Faulconbridge property experts and another saying WYNDALE your Lawson property experts and WYNDALE your Hazelbrook property experts (3 different versions all up ) and another version MAREE DOLTON your Faulconbridge property expert with logo and her image , i've put a photo of the top banner example and a video of the side banner it has a video in the background that i will get produced if it works

```html
<!DOCTYPE html>
<html lang="en">
<head>
<meta charset="utf-8">
<title>Wyndale – Your Lawson property experts</title>
<link href="https://fonts.googleapis.com/css2?family=Questrial&family=Oranienbaum&family=Roboto:wght@400;700&display=swap" rel="stylesheet">
<style>
  :root {
    --navy: #0b1152;
    --navy-soft: #1d2966;
    --white: #ffffff;
    --white-muted: #e9ebf4;
  }
  html, body {
    margin: 0;
    padding: 0;
    width: 1200px;
    height: 4504px;
    overflow: hidden;
    background: var(--navy);
  }
  .skyscraper {
    position: relative;
    width: 1200px;
    height: 4504px;
    background: var(--navy);
    overflow: hidden;
    color: var(--white);
  }
  .backdrop-arc {
    position: absolute;
    inset: 0;
    width: 1200px;
    height: 4504px;
  }
  .brand {
    position: absolute;
    top: 300px;
    left: 0;
    width: 100%;
    text-align: center;
  }
  .brand-mark {
    display: block;
    width: 88px;
    height: 88px;
    margin: 0 auto 96px;
    border: 8px solid var(--white-muted);
    box-sizing: border-box;
  }
  .brand-name {
    font-family: "Questrial", sans-serif;
    font-size: 128px;
    letter-spacing: 14px;
    line-height: 1;
    margin: 0;
    padding-left: 14px;
    color: var(--white-muted);
  }
  .brand-since {
    font-family: "Questrial", sans-serif;
    font-size: 44px;
    letter-spacing: 16px;
    line-height: 1;
    margin: 70px 0 0;
    padding-left: 16px;
    color: var(--white-muted);
  }
  .headline {
    position: absolute;
    top: 1540px;
    left: 0;
    width: 100%;
    margin: 0;
    text-align: center;
    font-family: "Oranienbaum", serif;
    font-weight: 400;
    font-size: 262px;
    line-height: 372px;
    color: var(--white);
  }
  .headline span { display: block; }
  .contact {
    position: absolute;
    top: 3800px;
    left: 0;
    width: 100%;
    text-align: center;
    font-family: "Roboto", Arial, sans-serif;
  }
  .contact-label {
    font-size: 82px;
    line-height: 1;
    margin: 0;
  }
  .contact-phone {
    font-size: 156px;
    font-weight: 700;
    line-height: 1;
    margin: 28px 0 0;
    letter-spacing: 2px;
  }
  .contact-web {
    font-size: 80px;
    line-height: 1;
    margin: 190px 0 0;
  }
</style>
</head>
<body>
  <main class="skyscraper">
    <svg class="backdrop-arc" viewBox="0 0 1200 4504" aria-hidden="true">
      <circle cx="1100" cy="2552" r="1536" fill="var(--navy-soft)"/>
    </svg>

    <header class="brand">
      <span class="brand-mark" aria-hidden="true"></span>
      <p class="brand-name">WYNDALE</p>
      <p class="brand-since">SINCE 1987</p>
    </header>

    <h1 class="headline">
      <span>Your</span>
      <span>Lawson</span>
      <span>property</span>
      <span>experts</span>
    </h1>

    <footer class="contact">
      <p class="contact-label">Contact</p>
      <p class="contact-phone">+614XXXXX</p>
      <p class="contact-web">www.yourwebsitename.com</p>
    </footer>
  </main>
</body>
</html>
```